Premium Juice and Wine Bottle Label

We require a premium label design for a Burgundy style wine bottle - the design should reflect pure and organic theme, with a reference to New Zealand blueberries. The winning design will look high-end, simple but sophisticated. Our logo is attached, refer :

https://www.orvalecellars.co.nz and https://www.pirovane.co.nz/wines/details/coming-soon-showcase/2018

for inspiration.

Target Market(s)

High-end retail grocery stores, wine shops, bars.

Requirements
Must have
• Label should leave enough space for barcode and nutrients/ingredients etc. Reference to New Zealand, natural-beverage, be very high-end in design. Refer links in project description for inspiration. Refer to attached logo, which must be used - feel free to change colour in order to obtain the best high-class design.
Nice to have
• N/A.
Should not have
• Cartoons or pictures of berries.

```html
<!DOCTYPE html>
<html lang="en">
<head>
<meta charset="utf-8">
<title>Marlow Grove Blueberry Wine Label</title>
<link rel="stylesheet" href="https://fonts.googleapis.com/css2?family=EB+Garamond:wght@400;700&family=Montserrat:wght@400&display=swap">
<style>
  :root {
    --backdrop: #8a72aa;
    --label-paper: #f8f2df;
    --brand-brown: #5a4a48;
    --ink-dark: #352c22;
    --ink-black: #111111;
    --ink-soft: #4a4038;
  }
  * { margin: 0; padding: 0; box-sizing: border-box; }
  html, body {
    width: 934px;
    height: 1200px;
    overflow: hidden;
    background: var(--backdrop);
  }
  .stage {
    position: relative;
    width: 934px;
    height: 1200px;
  }
  .label {
    position: absolute;
    left: 187px;
    top: 139px;
    width: 560px;
    height: 922px;
    background: var(--label-paper);
    box-shadow: 0 6px 24px rgba(60, 40, 80, 0.35);
    font-family: "EB Garamond", Georgia, serif;
    text-align: center;
  }
  .brand-mark {
    position: absolute;
    top: 96px;
    left: 0;
    right: 0;
    display: flex;
    justify-content: center;
    align-items: center;
    gap: 12px;
  }
  .brand-mark__square {
    width: 34px;
    height: 34px;
    background: var(--brand-brown);
  }
  .brand-mark__name {
    font-size: 26px;
    font-weight: 400;
    color: var(--brand-brown);
  }
  .brand-title {
    position: absolute;
    top: 178px;
    left: 0;
    right: 0;
    font-size: 80px;
    font-weight: 400;
    line-height: 1;
    color: var(--brand-brown);
  }
  .brand-established {
    position: absolute;
    top: 256px;
    left: 0;
    right: 0;
    font-family: "Montserrat", Arial, sans-serif;
    font-size: 22px;
    letter-spacing: 2px;
    color: var(--brand-brown);
  }
  .product-name {
    position: absolute;
    top: 536px;
    left: 0;
    right: 0;
    font-size: 42px;
    font-weight: 700;
    line-height: 63px;
    color: var(--ink-dark);
  }
  .product-name__type { color: var(--ink-black); }
  .product-tagline {
    position: absolute;
    top: 680px;
    left: 140px;
    right: 140px;
    font-size: 27px;
    line-height: 38px;
    color: var(--ink-soft);
  }
  .product-volume {
    position: absolute;
    top: 826px;
    left: 0;
    right: 0;
    font-size: 33px;
    color: var(--ink-soft);
  }
</style>
</head>
<body>
  <main class="stage">
    <section class="label">
      <div class="brand-mark">
        <span class="brand-mark__square"></span>
        <span class="brand-mark__name">Marlow Grove</span>
      </div>
      <h1 class="brand-title">Marlow Grove</h1>
      <p class="brand-established">Est 1987</p>
      <h2 class="product-name">BLUEBERRY<br><span class="product-name__type">WINE</span></h2>
      <p class="product-tagline">Real taste of New Zealand Blueberries</p>
      <p class="product-volume">Net wt 500ml</p>
    </section>
  </main>
</body>
</html>
```